Vexorun.co is a multi-sport platform that connects players, clubs, coaches, and organizers in one ecosystem.

Core value:
- Players can instantly find or create games across sports (padel, pickleball, tennis, soccer, etc.)
- Clubs can manage players, classes, staff, and tournaments in one place
- Coaches and organizers can create events and earn money directly through the platform

Key differentiator:
Vexorun is not just for finding games — it is a revenue engine for clubs and sports communities.

Main features to highlight:
- Find and join games instantly
- Create games without coordination friction
- Club management (players, classes, payments)
- Coaches offering lessons and programs
- Tournaments and events between clubs
- Fill empty court time with automated or quick-created events

Business model:
- Free to join
- Platform takes a small fee on transactions (events, classes, subscriptions)

Tagline:
“Let the Games Begin & Pick Your Challenge”

Tone:
Modern, premium, community-driven, and action-oriented.
Focus on simplicity, energy, and real usage scenarios.

Target Market(s)

multi-sport platform that connects players, clubs, coaches, and organizers in one ecosystem.

Industry/Entity Type

Sport

Coding

Coded - Design and coding required

Number of Pages Required

3 page

Requirements
Must have
• Build you the exact Webflow structure (class-by-class export)
Nice to have
• Html y css

```html
<!DOCTYPE html>
<html lang="en">
<head>
<meta charset="utf-8">
<title>Vexorun — The global network for players and clubs</title>
<link href="https://fonts.googleapis.com/css2?family=Poppins:wght@400;500;600;700;800&display=swap" rel="stylesheet">
<style>
:root{
  --lime:#9ad21f;
  --lime-soft:#7fb31a;
  --ink:#0b0e0c;
  --panel:rgba(22,26,22,.85);
  --panel-line:rgba(255,255,255,.1);
  --text:#ffffff;
  --muted:#b9c0b6;
  --screen:#0e110f;
  --screen-card:#1a1e1b;
  --footer:#0a0b0a;
}
*{margin:0;padding:0;box-sizing:border-box}
html,body{width:1200px;height:2824px;overflow:hidden;background:var(--ink)}
body{font-family:"Poppins",sans-serif;color:var(--text);position:relative}
.abs{position:absolute}
.lime{color:var(--lime)}
.nowrap{white-space:nowrap}

.hero-bg{left:0;top:0;width:1200px;height:1405px;background:radial-gradient(ellipse at 70% 30%,#2a3a44 0%,#17212a 35%,#0d1114 75%)}
.hero-bg::after{content:"";position:absolute;inset:0;background:linear-gradient(90deg,rgba(8,10,9,.75) 0%,rgba(8,10,9,.2) 60%,rgba(8,10,9,.4) 100%)}
.brand{display:flex;align-items:center;gap:12px;font-weight:600;font-size:32px;color:var(--text);white-space:nowrap}
.brand-dot{width:62px;height:62px;border-radius:50%;background:var(--lime);flex:none}
.nav{left:414px;top:38px;display:flex;gap:34px;font-size:14px;white-space:nowrap}
.nav a{color:var(--text);text-decoration:none}
.nav a.active{color:var(--lime);border-bottom:2px solid var(--lime);padding-bottom:4px}
.hero-title{left:75px;top:218px;font-size:56px;font-weight:800;line-height:56px;letter-spacing:-.5px;white-space:nowrap}
.hero-sub{left:75px;top:337px;font-size:24px;font-weight:500;line-height:33px;width:640px}
.btn{display:inline-flex;align-items:center;justify-content:center;height:44px;border-radius:22px;font-weight:600;font-size:16px;white-space:nowrap}
.btn-primary{background:var(--lime);color:#fff;width:166px}
.btn-outline{border:1.5px solid #fff;color:#fff;width:144px}
.flags{display:flex;gap:10px}
.flag{width:25px;text-align:center;font-size:7px;color:var(--muted)}
.flag i{display:block;width:25px;height:15px;margin-bottom:4px;border-radius:1px}

/* phone screens */
.phone{position:absolute;border-radius:26px;border:3px solid #3a3e3b;background:var(--screen);overflow:hidden;box-shadow:0 20px 50px rgba(0,0,0,.6);padding:9px 9px;font-size:8px;color:var(--text)}
.ph-status{display:flex;justify-content:space-between;font-size:8px;color:#ddd;padding:0 6px}
.ph-head{display:flex;align-items:center;gap:6px;font-size:13px;margin:10px 0 7px;white-space:nowrap}
.ph-head i{width:14px;height:14px;border-radius:50%;background:var(--lime);flex:none}
.ph-tabs{display:flex;gap:10px;font-size:7px;color:var(--muted);margin-bottom:6px;white-space:nowrap;border-bottom:1px solid var(--panel-line);padding-bottom:4px}
.ph-tabs .on{color:var(--lime)}
.ph-card{background:var(--screen-card);border-radius:8px;padding:6px 8px;margin-bottom:6px;color:var(--muted);line-height:1.35;white-space:nowrap;overflow:hidden}
.ph-card b{color:var(--text);font-weight:500}
.ph-row{display:flex;align-items:center;gap:6px;white-space:nowrap}
.ph-sub{font-size:6.5px;color:var(--muted)}
.av{width:22px;height:22px;border-radius:50%;background:linear-gradient(#6b665e,#3b3935);flex:none}
.stars{color:var(--lime);font-size:6px;letter-spacing:1px}
.ph-img{border-radius:6px;background:linear-gradient(160deg,#5b5a3a,#2a2c1d 55%,#121410)}
.ph-btn{background:var(--lime-soft);border-radius:6px;text-align:center;font-size:10px;padding:4px 0;margin:6px 0}
.ph-nav{position:absolute;bottom:14px;left:10px;right:10px;display:flex;justify-content:space-between;font-size:5.5px;color:#aaa;white-space:nowrap}
.ph-nav span{text-align:center}
.ph-nav span::before{content:"";display:block;width:9px;height:9px;border:1.3px solid #bbb;border-radius:50%;margin:0 auto 3px}
.ph-nav .on{color:var(--lime)}
.ph-nav .on::before{border-color:var(--lime);background:var(--lime)}

.section-title{width:1200px;text-align:center;font-weight:700;font-size:34px;white-space:nowrap}
.bar{left:232px;width:739px;height:80px;background:var(--panel);border-radius:14px}
.bar-item{position:absolute;top:0;height:80px;display:flex;align-items:center;font-size:15px;font-weight:500;line-height:19px;white-space:nowrap}
.f-ico{position:absolute;top:22px;width:36px;height:36px;border:1.5px solid var(--lime);border-radius:50%;display:flex;align-items:center;justify-content:center}
.bar-split{position:absolute;left:0;top:0;width:121px;height:80px;border-right:1px solid var(--panel-line);display:flex;align-items:center;padding-left:19px;font-weight:700;font-size:19px;line-height:22px}

.aud-bg{left:0;top:1405px;width:1200px;height:379px;background:linear-gradient(180deg,#152018,#1a2a1e 50%,#101512)}
.card{top:1527px;width:329px;height:197px;background:rgba(15,18,15,.8);border-radius:14px;padding:16px 18px}
.card-head{display:flex;align-items:center;gap:16px;font-size:21px;font-weight:700;color:var(--lime);margin-bottom:20px;white-space:nowrap}
.card-ico{width:50px;height:50px;border-radius:10px;background:var(--lime-soft);display:flex;align-items:center;justify-content:center}
.card li{list-style:none;display:flex;align-items:center;gap:12px;font-size:16px;margin:0 0 12px 6px;white-space:nowrap}

.map-bg{left:0;top:1784px;width:1200px;height:813px;background:radial-gradient(ellipse at 50% 40%,#1d2a12 0%,#0e130b 60%,#090b08)}
.map-area{left:219px;top:2040px;width:878px;height:450px;border-radius:48%;background:radial-gradient(ellipse at 50% 45%,#2b3822 0%,#1c2616 45%,rgba(20,27,15,.6) 65%,transparent 75%)}

.footer{left:0;top:2597px;width:1200px;height:227px;background:var(--footer)}
.f-col{position:absolute}
.f-col h4{font-size:16px;font-weight:600;line-height:24px;margin-bottom:7px;white-space:nowrap}
.f-col a{display:block;color:var(--text);text-decoration:none;font-size:14px;line-height:21px;margin-bottom:9.6px;white-space:nowrap}
.social{display:flex;gap:22px;margin-top:10px}
.social span{width:24px;height:24px;border-radius:50%;background:#fff;display:block}
</style>
</head>
<body>
<div class="abs hero-bg" role="img" aria-label="Night-time padel court photograph with glass walls and stadium lights"></div>

<header>
  <div class="abs brand" style="left:75px;top:20px"><span class="brand-dot"></span>Vexorun</div>
  <nav class="abs nav">
    <a class="active" href="#">Home</a><a href="#">Find Matches</a><a href="#">Events &amp; Tournaments</a><a href="#">Clubs</a><a href="#">How It Works</a><a href="#">Pricing</a><a href="#">Locations</a>
  </nav>
</header>

<h1 class="abs hero-title">The global network<br>for <span class="lime">players and clubs</span></h1>
<p class="abs hero-sub">Find games. Join events. Connect with the sports community anywhere in the world.</p>
<div class="abs" style="left:75px;top:427px;display:flex;gap:13px">
  <span class="btn btn-primary">Join as Player</span><span class="btn btn-outline">Join as Club</span>
</div>
<p class="abs nowrap" style="left:74px;top:511px;font-size:17px;font-weight:500">Built for <b class="lime">Pickleball &amp; Padel</b>. Expanding to all sports.</p>
<div class="abs flags" style="left:73px;top:545px">
  <div class="flag"><i style="background:linear-gradient(#1f3b8f 0 35%,#fff 35% 65%,#1f3b8f 65%)"></i>Dolore</div>
  <div class="flag"><i style="background:linear-gradient(90deg,#1f3b8f 33%,#fff 33% 66%,#d42a2a 66%)"></i>Dolore</div>
  <div class="flag"><i style="background:linear-gradient(#0a8a3a 33%,#fff 33% 66%,#111 66%)"></i>Dolore</div>
  <div class="flag"><i style="background:linear-gradient(#f39a2a 33%,#fff 33% 66%,#138a2a 66%)"></i>Dolore</div>
  <div class="flag"><i style="background:linear-gradient(#1e5aa8 40%,#f5c400 40% 60%,#1e5aa8 60%)"></i>Dolore</div>
  <div class="flag"><i style="background:linear-gradient(#c8202e 33%,#fff 33% 66%,#203a8a 66%)"></i>Dolore</div>
  <div class="flag"><i style="background:radial-gradient(circle,#c8202e 30%,#fff 32%)"></i>Dolore</div>
  <div class="flag"><i style="background:linear-gradient(#111 30%,#c8202e 30% 70%,#0a7a3a 70%)"></i>Dolore</div>
  <div class="flag"><i style="background:linear-gradient(#111 33%,#d42a2a 33% 66%,#f5c400 66%)"></i>Dolore</div>
  <div class="flag"><i style="background:linear-gradient(#c8202e 25%,#f5c400 25% 75%,#c8202e 75%)"></i>Dolore</div>
  <div class="flag"><i style="background:linear-gradient(#111 30%,#c8202e 30% 70%,#0a7a3a 70%)"></i>Dolore</div>
  <div class="flag"><i style="background:linear-gradient(90deg,#0a7a3a 40%,#d42a2a 40%)"></i>Dolore</div>
</div>

<!-- hero app screen -->
<div class="phone" style="left:756px;top:130px;width:238px;height:484px;border-radius:34px;border-width:4px;transform:rotate(-3deg);padding:14px 13px">
  <div class="ph-status"><span>9:41</span><span>●●● ▮</span></div>
  <div class="ph-head" style="font-size:16px"><i style="width:18px;height:18px"></i>Vexorun</div>
  <div class="ph-card ph-row" style="font-size:7.5px"><span class="lime">●</span>10,585 Players Online · 1,482</div>
  <div class="ph-card ph-row" style="background:linear-gradient(90deg,#3f6a14,#2b4a10);padding:9px 10px">
    <svg width="26" height="26" viewBox="0 0 26 26"><circle cx="13" cy="13" r="12" fill="none" stroke="#9ad21f" stroke-width="2"/><path d="M10 8l8 5-8 5z" fill="#9ad21f"/></svg>
    <div><b style="font-size:13px;display:block">Play Now</b><span class="ph-sub" style="color:#dfe8cf">Start playing instantly</span></div>
  </div>
  <div class="ph-row ph-sub" style="margin:2px 0 10px 4px"><span class="lime">●</span>18,533 Players · 247 Games available</div>
  <div class="ph-card" style="padding:9px 10px">
    <b style="font-size:12px;display:block;margin-bottom:3px">Find Matches</b>
    <div class="ph-sub">• Play instantly or schedule games</div>
    <div class="ph-sub">• Match with players at your level</div>
  </div>
  <div class="ph-card ph-row" style="justify-content:space-between"><span><span class="lime">●</span> <b>Bayview Park</b></span><span style="background:#2a2f2b;border-radius:8px;padding:1px 8px;color:#fff">See All</span></div>
  <div class="ph-card">
    <div class="ph-row" style="margin-bottom:7px"><span class="av"></span><div style="flex:1"><b style="font-size:9px">Sandro Close</b><div class="ph-sub">Intermediate</div><div class="stars">★★★★</div></div><span class="ph-sub">3 miles away</span></div>
    <div class="ph-row" style="margin-bottom:7px"><span class="av"></span><div style="flex:1"><b style="font-size:9px">Sofia</b><div class="ph-sub">Beginner</div><div class="stars">★★★★★</div></div><span class="ph-sub">1 mile away</span></div>
    <div class="ph-row"><span class="av"></span><div style="flex:1"><b style="font-size:9px">Jeremy Mills</b><div class="ph-sub">Intermediate</div><div class="stars">★★★★★</div></div><span class="ph-sub">Available Now</span></div>
  </div>
  <div class="ph-nav" style="bottom:22px;font-size:6.5px"><span class="on">Home</span><span>Matches</span><span>Events</span><span>Messages</span><span>Profile</span></div>
</div>

<h2 class="abs section-title" style="top:705px">Everything in your sport. <span class="lime">One place.</span></h2>
<div class="abs bar" style="top:778px">
  <div class="bar-split">Find<br>Matches</div>
  <span class="f-ico" style="left:135px"><svg width="16" height="16" viewBox="0 0 16 16"><path d="M2 7h3v7H2zM6 7l3-5c1 0 2 1 1.5 3H14l-1 8H6z" fill="#9ad21f"/></svg></span>
  <div class="bar-item" style="left:186px">Find matches<br>instantly</div>
  <span class="f-ico" style="left:311px"><svg width="16" height="16" viewBox="0 0 16 16"><path d="M3 13V8M7 13V4M11 13V6M2 14h12" stroke="#9ad21f" stroke-width="1.6" fill="none"/></svg></span>
  <div class="bar-item" style="left:363px">Match with players<br>at your skill level</div>
  <span class="f-ico" style="left:522px"><svg width="16" height="16" viewBox="0 0 16 16"><rect x="2" y="3" width="12" height="11" rx="1.5" stroke="#9ad21f" stroke-width="1.5" fill="none"/><path d="M2 6h12M5 1v3M11 1v3" stroke="#9ad21f" stroke-width="1.5"/></svg></span>
  <div class="bar-item" style="left:574px">Play instantly<br>or schedule games</div>
</div>

<!-- app screens row -->
<div class="phone" style="left:287px;top:904px;width:142px;height:350px">
  <div class="ph-status"><span>9:41</span><span>▮</span></div>
  <div class="ph-head"><i></i>Matches</div>
  <div class="ph-tabs"><span class="on">Nearby Now</span><span>Played</span></div>
  <div class="ph-card"><b>Bayview Park</b></div>
  <div class="ph-card"><b>Intermediate</b></div>
  <div class="ph-row" style="margin:6px 0 2px"><span class="av"></span><div><b style="font-size:8.5px;font-weight:500">Kai Nguyen</b><div class="ph-sub">Intermediate</div></div></div>
  <div class="ph-sub" style="margin-bottom:6px">2.3 km · Open 2 spots</div>
  <div class="ph-row" style="margin-bottom:2px"><span class="av"></span><div><b style="font-size:8.5px;font-weight:500">Jeremy Wills</b><div class="ph-sub">Advanced</div></div></div>
  <div class="ph-sub" style="margin-bottom:6px">4.8 km · Doubles</div>
  <div class="ph-row" style="margin-bottom:2px"><span class="av"></span><div><b style="font-size:8.5px;font-weight:500">Jae Kim</b><div class="ph-sub">Beginner</div></div></div>
  <div class="ph-sub">6 km · Open Today</div>
  <div class="ph-nav"><span class="on">Home</span><span>Matches</span><span>Events</span></div>
</div>

<div class="phone" style="left:427px;top:904px;width:130px;height:350px">
  <div class="ph-status"><span>9:41</span><span>▮</span></div>
  <div class="ph-head"><i></i>Events</div>
  <div class="ph-tabs"><span class="on">All Sports</span><span>Nearest First</span></div>
  <div class="ph-img" style="height:60px;margin-bottom:6px" role="img" aria-label="Event photo of an indoor court"></div>
  <b style="font-size:10px;font-weight:500;display:block;white-space:nowrap">Pickleball Tourney</b>
  <div class="ph-sub" style="margin-bottom:4px">Sat 10:00 AM · 32 spots</div>
  <div class="ph-card" style="margin-top:8px"><b style="font-size:10px">Drop in Padel</b><div class="ph-sub">Beginner friendly</div></div>
  <div class="ph-sub" style="margin:2px 0 4px">Jun 10, 6:00 PM</div>
  <div class="ph-sub">Jun 21 · 8 players</div>
  <div class="ph-nav"><span class="on">Home</span><span>Matches</span><span>Events</span></div>
</div>

<div class="phone" style="left:556px;top:902px;width:174px;height:352px;z-index:2;border-color:#4a4f4b">
  <div class="ph-status"><span>9:41</span><span>●●● ▮</span></div>
  <div class="ph-head" style="font-size:14px"><i></i>Vexorun</div>
  <div class="ph-img" style="height:112px;padding:8px;position:relative" role="img" aria-label="Photo of a lit outdoor court at night">
    <b style="font-size:13px;font-weight:500;white-space:nowrap">Evening Matches</b>
    <div class="ph-sub" style="color:#dcdcc8">Intermediate · Tonight</div>
  </div>
  <div class="ph-row" style="justify-content:space-between;margin:8px 2px 4px"><b style="font-size:10px;font-weight:500">4 – 6 players</b><span class="ph-sub">Intermediate</span></div>
  <div class="ph-sub" style="margin:0 2px 6px">Open match · 2 spots left</div>
  <div class="ph-row" style="gap:12px;margin:0 4px">
    <div style="text-align:center"><span class="av" style="display:block;width:28px;height:28px;margin:0 auto 2px"></span><span class="ph-sub">Jordan</span></div>
    <div style="text-align:center"><span class="av" style="display:block;width:28px;height:28px;margin:0 auto 2px"></span><span class="ph-sub">Daniel</span></div>
    <div style="text-align:center"><span style="display:block;width:28px;height:28px;border-radius:50%;background:#2a2e2b;margin:0 auto 2px;line-height:28px;font-size:12px;color:#888">?</span><span class="ph-sub">Open</span></div>
    <div style="text-align:center"><span style="display:block;width:28px;height:28px;border-radius:50%;background:#2a2e2b;margin:0 auto 2px;line-height:28px;font-size:12px;color:#888">?</span><span class="ph-sub">Open</span></div>
  </div>
  <div class="ph-btn" style="margin-top:12px">Join Match</div>
  <div class="ph-card ph-row"><span class="lime">●</span><div><b>Game Details</b><div class="ph-sub">Location, rules and court info</div></div></div>
</div>

<div class="phone" style="left:731px;top:906px;width:182px;height:348px">
  <div class="ph-status"><span>9:41</span><span>●●● ▮</span></div>
  <div class="ph-head"><i></i>Schedule</div>
  <div class="ph-tabs"><span>Upcoming</span><span class="on">Reserved</span><span>Past</span></div>
  <div class="ph-card ph-row" style="align-items:flex-start"><span class="av"></span><div><b>Nov 13 · Confirmed</b><div class="ph-sub">Weekly open play at 7 PM</div><div class="ph-sub">Harbor Courts, court 3</div></div></div>
  <div class="ph-row ph-sub" style="justify-content:space-between;margin:8px 2px 6px"><span>Today</span><span>April 16</span></div>
  <div class="ph-card">
    <b style="font-size:9.5px">Thursday April 16</b><br><b style="font-size:9.5px">5:30 PM</b>
    <div class="ph-sub">Reserved Doubles</div>
    <div class="ph-sub"><span class="lime">●</span> Harbor Courts</div>
    <div class="ph-row" style="justify-content:space-between;margin-top:8px"><b>2:30 PM</b><span>Full</span><span style="background:var(--lime-soft);color:#fff;border-radius:6px;padding:1px 8px">Join</span></div>
  </div>
  <div class="ph-card" style="text-align:center">View Past Matches ›</div>
  <div class="ph-nav"><span class="on">Home</span><span>Matches</span><span>Events</span><span>Profile</span></div>
</div>

<div class="abs" style="left:880px;top:1095px;width:320px;height:310px;background:radial-gradient(ellipse at 70% 50%,#4a4e52,#1a1d1e 60%,transparent 75%)" role="img" aria-label="Player swinging a padel racket at a yellow ball"></div>

<p class="abs" style="left:0;top:1289px;width:1200px;text-align:center;font-size:13px;font-weight:500">Now available in 12+ locations</p>
<div class="abs flags" style="left:484px;top:1326px">
  <div class="flag"><i style="background:linear-gradient(#1f3b8f 0 35%,#fff 35% 65%,#1f3b8f 65%)"></i>Dolore</div>
  <div class="flag"><i style="background:linear-gradient(90deg,#1f3b8f 33%,#fff 33% 66%,#d42a2a 66%)"></i>Dolore</div>
  <div class="flag"><i style="background:linear-gradient(#0a8a3a 33%,#fff 33% 66%,#111 66%)"></i>Dolore</div>
  <div class="flag"><i style="background:linear-gradient(#f39a2a 33%,#fff 33% 66%,#138a2a 66%)"></i>Dolore</div>
  <div class="flag"><i style="background:linear-gradient(#1e5aa8 40%,#f5c400 40% 60%,#1e5aa8 60%)"></i>Dolore</div>
  <div class="flag"><i style="background:linear-gradient(#c8202e 33%,#fff 33% 66%,#203a8a 66%)"></i>Dolore</div>
  <div class="flag"><i style="background:radial-gradient(circle,#c8202e 30%,#fff 32%)"></i>Dolore</div>
</div>

<div class="abs aud-bg" role="img" aria-label="Blurred green sports field background"></div>
<h2 class="abs section-title" style="top:1457px">Built for how people actually <span class="lime">play sports</span></h2>
<div class="abs card" style="left:75px">
  <div class="card-head"><span class="card-ico"><svg width="22" height="22" viewBox="0 0 22 22"><circle cx="11" cy="7" r="5" fill="#fff"/><path d="M2 21c0-5 4-8 9-8s9 3 9 8z" fill="#fff"/></svg></span>For Players</div>
  <ul><li><svg width="15" height="15" viewBox="0 0 16 16"><circle cx="8" cy="8" r="7" stroke="#9ad21f" stroke-width="1.5" fill="none"/><path d="M5 8l2 2 4-4" stroke="#9ad21f" stroke-width="1.6" fill="none"/></svg>Find games instantly</li><li><svg width="15" height="15" viewBox="0 0 16 16"><circle cx="8" cy="8" r="7" stroke="#9ad21f" stroke-width="1.5" fill="none"/><path d="M5 8l2 2 4-4" stroke="#9ad21f" stroke-width="1.6" fill="none"/></svg>Meet players</li><li><svg width="15" height="15" viewBox="0 0 16 16"><circle cx="8" cy="8" r="7" stroke="#9ad21f" stroke-width="1.5" fill="none"/><path d="M5 8l2 2 4-4" stroke="#9ad21f" stroke-width="1.6" fill="none"/></svg>Grow your community</li></ul>
</div>
<div class="abs card" style="left:436px">
  <div class="card-head"><span class="card-ico"><svg width="26" height="22" viewBox="0 0 26 22"><circle cx="13" cy="7" r="4" fill="#fff"/><circle cx="5" cy="9" r="3" fill="#fff"/><circle cx="21" cy="9" r="3" fill="#fff"/><path d="M6 20c0-4 3-7 7-7s7 3 7 7zM0 19c0-3 2-5 5-5l1 1-2 4zM26 19c0-3-2-5-5-5l-1 1 2 4z" fill="#fff"/></svg></span>For Clubs</div>
  <ul><li><svg width="15" height="15" viewBox="0 0 16 16"><circle cx="8" cy="8" r="7" stroke="#9ad21f" stroke-width="1.5" fill="none"/><path d="M5 8l2 2 4-4" stroke="#9ad21f" stroke-width="1.6" fill="none"/></svg>Fill courts</li><li><svg width="15" height="15" viewBox="0 0 16 16"><circle cx="8" cy="8" r="7" stroke="#9ad21f" stroke-width="1.5" fill="none"/><path d="M5 8l2 2 4-4" stroke="#9ad21f" stroke-width="1.6" fill="none"/></svg>Manage players</li><li><svg width="15" height="15" viewBox="0 0 16 16"><circle cx="8" cy="8" r="7" stroke="#9ad21f" stroke-width="1.5" fill="none"/><path d="M5 8l2 2 4-4" stroke="#9ad21f" stroke-width="1.6" fill="none"/></svg>Grow your community</li></ul>
</div>
<div class="abs card" style="left:797px">
  <div class="card-head"><span class="card-ico"><svg width="22" height="22" viewBox="0 0 22 22"><path d="M11 1l10 5H1z M3 8h2v9H3zM8 8h2v9H8zM12 8h2v9h-2zM17 8h2v9h-2zM1 19h20v2H1z" fill="#fff"/></svg></span>For Organizers</div>
  <ul><li><svg width="15" height="15" viewBox="0 0 16 16"><circle cx="8" cy="8" r="7" stroke="#9ad21f" stroke-width="1.5" fill="none"/><path d="M5 8l2 2 4-4" stroke="#9ad21f" stroke-width="1.6" fill="none"/></svg>Run events</li><li><svg width="15" height="15" viewBox="0 0 16 16"><circle cx="8" cy="8" r="7" stroke="#9ad21f" stroke-width="1.5" fill="none"/><path d="M5 8l2 2 4-4" stroke="#9ad21f" stroke-width="1.6" fill="none"/></svg>Leagues</li><li><svg width="15" height="15" viewBox="0 0 16 16"><circle cx="8" cy="8" r="7" stroke="#9ad21f" stroke-width="1.5" fill="none"/><path d="M5 8l2 2 4-4" stroke="#9ad21f" stroke-width="1.6" fill="none"/></svg>Tournaments</li></ul>
</div>

<div class="abs map-bg" role="img" aria-label="Dark textured grass background"></div>
<h2 class="abs section-title" style="top:1827px">Launching city by city <span class="lime">worldwide</span></h2>
<div class="abs bar" style="top:1900px">
  <span class="f-ico" style="left:42px;border-color:rgba(255,255,255,.5)"><svg width="16" height="16" viewBox="0 0 16 16"><circle cx="8" cy="8" r="6.5" stroke="#fff" stroke-width="1.3" fill="none"/><path d="M1.5 8h13M8 1.5c3 3 3 10 0 13M8 1.5c-3 3-3 10 0 13" stroke="#fff" stroke-width="1.2" fill="none"/></svg></span>
  <div class="bar-item" style="left:92px">Building the first global<br>sports network</div>
  <span class="f-ico" style="left:303px;border-color:rgba(255,255,255,.5)"><svg width="16" height="16" viewBox="0 0 16 16"><ellipse cx="10" cy="6" rx="4.5" ry="4.5" stroke="#fff" stroke-width="1.3" fill="none"/><path d="M7 9l-5 5" stroke="#fff" stroke-width="2"/></svg></span>
  <div class="bar-item" style="left:354px">Starting with<br>Pickleball &amp; Padel</div>
  <span class="f-ico" style="left:532px;border-color:rgba(255,255,255,.5)"><svg width="16" height="16" viewBox="0 0 16 16"><rect x="6" y="1" width="4" height="4" fill="#fff"/><rect x="1" y="10" width="4" height="4" fill="#fff"/><rect x="11" y="10" width="4" height="4" fill="#fff"/><path d="M8 5v3M3 10V8h10v2" stroke="#fff" stroke-width="1.3" fill="none"/></svg></span>
  <div class="bar-item" style="left:583px">Expanding to all<br>sports</div>
</div>
<div class="abs map-area" role="img" aria-label="Dark world map showing the continents, with launch city markers"></div>
<svg class="abs" style="left:0;top:0" width="1200" height="2824" aria-hidden="true">
  <defs><path id="pin" d="M0 0c-6 0-10 4.5-10 10 0 7 10 16 10 16s10-9 10-16c0-5.5-4-10-10-10z M0 6a4 4 0 1 0 0.01 0z" fill="#9ad21f" fill-rule="evenodd"/></defs>
  <use href="#pin" x="494" y="2058"/><use href="#pin" x="334" y="2117"/><use href="#pin" x="805" y="2212"/><use href="#pin" x="448" y="2319"/><use href="#pin" x="644" y="2338"/>
</svg>
<div class="abs flags" style="left:433px;top:2505px">
  <div class="flag"><i style="background:linear-gradient(#1f3b8f 0 35%,#fff 35% 65%,#1f3b8f 65%)"></i>Dolore</div>
  <div class="flag"><i style="background:linear-gradient(90deg,#1f3b8f 33%,#fff 33% 66%,#d42a2a 66%)"></i>Dolore</div>
  <div class="flag"><i style="background:linear-gradient(#0a8a3a 33%,#fff 33% 66%,#111 66%)"></i>Dolore</div>
  <div class="flag"><i style="background:linear-gradient(#f39a2a 33%,#fff 33% 66%,#138a2a 66%)"></i>Dolore</div>
  <div class="flag"><i style="background:linear-gradient(#1e5aa8 40%,#f5c400 40% 60%,#1e5aa8 60%)"></i>Dolore</div>
  <div class="flag"><i style="background:linear-gradient(#c8202e 33%,#fff 33% 66%,#203a8a 66%)"></i>Dolore</div>
  <div class="flag"><i style="background:radial-gradient(circle,#c8202e 30%,#fff 32%)"></i>Dolore</div>
  <div class="flag"><i style="background:linear-gradient(#111 30%,#c8202e 30% 70%,#0a7a3a 70%)"></i>Dolore</div>
  <div class="flag"><i style="background:linear-gradient(#111 33%,#d42a2a 33% 66%,#f5c400 66%)"></i>Dolore</div>
  <div class="flag"><i style="background:linear-gradient(#c8202e 25%,#f5c400 25% 75%,#c8202e 75%)"></i>Dolore</div>
</div>

<footer class="abs footer">
  <div class="abs brand" style="left:75px;top:66px;font-size:30px"><span class="brand-dot" style="width:58px;height:58px"></span>Vexorun</div>
  <p class="abs" style="left:75px;top:130px;font-size:12px;line-height:21px;white-space:nowrap">Copyright © 2026 Vexorun.co<br>All Rights Reserved</p>
  <div class="f-col" style="left:343px;top:55px"><h4>Quick Links</h4><a>Home</a><a>Find Matches</a><a>Events &amp; Tournaments</a><a>Clubs</a></div>
  <div class="f-col" style="left:534px;top:86px"><a>How It Works</a><a>Pricing</a><a>Locations</a></div>
  <div class="f-col" style="left:705px;top:55px"><h4>Resources</h4><a>Excepteur sint</a><a>Occaecat cupidatat</a><a>Non proident</a><a>Commodo</a></div>
  <div class="f-col" style="left:920px;top:55px"><h4>Follow Us</h4><div class="social"><span></span><span></span><span></span><span></span></div></div>
</footer>
</body>
</html>
```